Flyer für Anbieter einer Fortbildung für Beratungslehrer
Zielgruppe
Wir bieten eine Fortbildung für Beratungslehrer an, welche mit immer komplexer werdenden psychischen Fällen arbeiten. Diese Fortbildung setzt sich gezielt mit der Stärkung des Selbstkonzepts, der Resilienz sowie dem Selbstwert auseinander. Wir stellen dabei die Anliegen der Klienten in den Fokus.
Das Angebot basiert auf dem Konzept des Lernfeld Zuversicht des Kurt- Wendland-Institut, Heidelberg
Aufgabenstellung
Die Inhalte der Fortbildung sollen enthalten sein.
Layout sollte unseren Arbeitsbereich im psychologischen Wohlbefinden widerspiegeln

```html
<!DOCTYPE html>
<html lang="de">
<head>
<meta charset="utf-8">
<title>Flyer – Fortbildung für Beratungslehrer</title>
<link rel="stylesheet" href="https://fonts.googleapis.com/css2?family=Montserrat:ital,wght@0,400;0,500;0,600;0,700;1,400&display=swap">
<style>
  :root {
    --teal: #5a9a8c;
    --white: #ffffff;
    --panel: rgba(240, 244, 240, 0.86);
    --text: #3c3c3c;
    --canvas: #ffffff;
    --forest-light: #b9cf5e;
    --forest-mid: #5f8f3a;
    --forest-dark: #2f5a2e;
    --water: #3f8a84;
  }
  * { box-sizing: border-box; margin: 0; padding: 0; }
  html, body { width: 1200px; height: 2400px; overflow: hidden; background: var(--canvas); }
  body { font-family: "Montserrat", sans-serif; color: var(--text); position: relative; }

  .spread { position: absolute; left: 60px; width: 1080px; height: 762px; overflow: hidden; }
  .spread--outside { top: 380px; }
  .spread--inside { top: 1240px; }

  .forest-photo {
    position: absolute;
    background:
      radial-gradient(ellipse at 45% 8%, rgba(230, 240, 130, 0.85), transparent 45%),
      linear-gradient(180deg, var(--forest-light) 0%, var(--forest-mid) 35%, var(--forest-dark) 62%, #4e6b45 74%, var(--water) 84%, #2e6c68 100%);
  }

  /* Outside spread */
  .back-cover { position: absolute; left: 0; top: 0; width: 540px; height: 762px; background: var(--teal); color: var(--white); }
  .front-cover { left: 540px; top: 0; width: 540px; height: 762px; }

  .brand { position: absolute; left: 0; width: 540px; text-align: center; color: var(--white); font-size: 22px; font-weight: 500; letter-spacing: 0.08em; text-transform: uppercase; }
  .back-cover .brand { top: 140px; }
  .front-cover .brand { top: 622px; }

  .back-cover__info { position: absolute; left: 0; width: 540px; top: 638px; text-align: center; font-size: 15px; line-height: 1.15; }
  .back-cover__info strong { font-weight: 700; display: block; }

  .title-frame { position: absolute; left: 51px; top: 76px; width: 438px; height: 242px; }
  .title-frame__corner { position: absolute; border-color: var(--white); border-style: solid; }
  .title-frame__corner--tl { left: 0; top: 0; width: 88px; height: 230px; border-width: 4px 0 0 4px; }
  .title-frame__corner--bl { left: 0; bottom: 0; width: 24px; height: 24px; border-width: 0 0 4px 4px; }
  .title-frame__corner--tr { right: 0; top: 0; width: 24px; height: 24px; border-width: 4px 4px 0 0; }
  .title-frame__corner--br { right: 0; bottom: 0; width: 88px; height: 230px; border-width: 0 4px 4px 0; }
  .title-box { position: absolute; left: 20px; top: 21px; width: 396px; height: 198px; background: var(--white); text-align: center; padding-top: 34px; }
  .title-box__headline { color: var(--teal); font-weight: 700; font-size: 15px; line-height: 1.25; text-transform: uppercase; }
  .title-box__sub { color: var(--teal); font-weight: 500; font-size: 17px; margin-top: 18px; }
  .title-box__topic { font-style: italic; font-size: 14px; line-height: 1.3; margin-top: 16px; color: #444; }

  /* Inside spread */
  .inside-photo { left: 0; top: 0; width: 1080px; height: 762px; }
  .intro-band { position: absolute; left: 0; top: 0; width: 540px; height: 173px; background: var(--teal); color: var(--white); padding: 40px 20px 0 76px; font-size: 17.5px; line-height: 1.15; font-weight: 500; }
  .info-tab { position: absolute; right: 0; top: 0; width: 210px; height: 58px; }
  .info-tab__label { position: absolute; right: 64px; top: 17px; color: var(--white); font-size: 15px; font-weight: 500; }

  .content-panel { position: absolute; background: var(--panel); padding: 34px 30px; font-size: 14px; line-height: 1.4; }
  .content-panel--left { left: 46px; top: 173px; width: 458px; height: 552px; }
  .content-panel--right { left: 575px; top: 173px; width: 460px; height: 402px; }
  .content-panel h2 { color: var(--teal); font-size: 17px; font-weight: 700; text-transform: uppercase; line-height: 1.15; margin-bottom: 14px; }
  .content-panel p { text-align: justify; margin-bottom: 32px; }
  .benefit { margin-bottom: 10px; }
  .benefit h3 { color: var(--teal); font-weight: 400; font-size: 14px; margin-bottom: 4px; }
  .benefit p { margin-bottom: 0; }

  .call-band { position: absolute; left: 555px; top: 575px; width: 525px; height: 187px; }
  .call-band svg { display: block; }
  .call-band__text { position: absolute; left: 90px; top: 54px; width: 420px; color: var(--white); font-size: 20px; font-weight: 500; line-height: 1.15; }
</style>
</head>
<body>

<section class="spread spread--outside">
  <div class="back-cover">
    <p class="brand">Zuversicht stärken</p>
    <p class="back-cover__info"><strong>Mehr Informationen auf</strong>www.zuversicht-staerken.de</p>
  </div>
  <div class="forest-photo front-cover" role="img" aria-label="Foto: sonniger Laubwald mit klarem, türkisfarbenem Bach im Vordergrund">
    <div class="title-frame">
      <span class="title-frame__corner title-frame__corner--tl"></span>
      <span class="title-frame__corner title-frame__corner--tr"></span>
      <span class="title-frame__corner title-frame__corner--bl"></span>
      <span class="title-frame__corner title-frame__corner--br"></span>
      <div class="title-box">
        <h1 class="title-box__headline">Stärkung des Selbstkonzepts,<br>des Selbstwerts und der Resilienz</h1>
        <p class="title-box__sub">Fortbildung für Beratungslehrer</p>
        <p class="title-box__topic">Stärkung des Selbstkonzepts,<br>des Selbstwerts und der Resilienz</p>
      </div>
    </div>
    <p class="brand">Zuversicht stärken</p>
  </div>
</section>

<section class="spread spread--inside">
  <div class="forest-photo inside-photo" role="img" aria-label="Foto: unscharfer, sonnendurchfluteter Wald als Hintergrund"></div>

  <div class="intro-band">Sie sind Beratungslehrer und möchten Ihre<br>Klient*innen bestmöglich in ihrer<br>persönlichen Entwicklung unterstützen?<br>Dann ist diese Fortbildung genau das<br>Richtige für Sie!</div>

  <svg class="info-tab" viewBox="0 0 210 58" aria-hidden="true"><polygon points="22,0 210,0 210,58 0,58" fill="var(--teal)"/></svg>
  <span class="info-tab__label">Information</span>

  <article class="content-panel content-panel--left">
    <h2>Inhalt der Fortbildung</h2>
    <p>In dieser praxisorientierten Fortbildung lernen Sie, wie Sie Ihre Klient*innen gezielt in den Bereichen Selbstkonzept, Selbstwert und Resilienz stärken können. Basierend auf dem bewährten Konzept des Lernfelds Zuversicht werden Ihnen Methoden und Techniken vermittelt, die direkt in der Beratung anwendbar sind.</p>
    <h2>Was erwartet Sie?</h2>
    <div class="benefit"><h3>1. Stärkung des Selbstkonzepts:</h3><p>Erfahren Sie, wie Sie Klient*innen helfen können, ein gesundes und positives Selbstbild zu entwickeln.</p></div>
    <div class="benefit"><h3>2. Aufbau von Selbstwert:</h3><p>Entdecken Sie Wege, um das Selbstvertrauen und die Eigenmotivation Ihrer Klient*innen nachhaltig zu fördern.</p></div>
    <div class="benefit"><h3>3. Förderung der Resilienz</h3><p>Lernen Sie Strategien kennen, mit denen Klient*innen Krisen und Herausforderungen besser bewältigen können.</p></div>
  </article>

  <article class="content-panel content-panel--right">
    <h2>Warum das Lernfeld Zuversicht?</h2>
    <p>Das Lernfeld Zuversicht verbindet positive Psychologie mit pädagogischen Ansätzen und ermöglicht eine ganzheitliche Förderung der Persönlichkeit. Ziel ist es, Klient*innen auf ein erfülltes und zufriedenes Leben vorzubereiten.</p>
    <h2>Für wen ist die<br>Fortbildung geeignet?</h2>
    <p>Diese Fortbildung richtet sich an Beratungslehrer, Schulpsychologen und pädagogische Fachkräfte, die ihre Kompetenzen erweitern und ihre Klient*innen bestmöglich unterstützen möchten.</p>
  </article>

  <div class="call-band">
    <svg width="525" height="187" viewBox="0 0 525 187" aria-hidden="true"><polygon points="55,0 525,0 525,187 0,187" fill="var(--teal)"/></svg>
    <p class="call-band__text">Investieren Sie in die Zukunft<br>Ihrer Klient*innen – und in Ihre<br>eigene Weiterbildung!</p>
  </div>
</section>

</body>
</html>
```